依頼詳細
設立間もない協会のため、初めての名刺作成となります。名刺を利用するのは、主に女性(看護師)となり、前述した当協会の認定講師です。派手過ぎず上品なデザインを求めます。左に写真を掲載したいと思います。
記載項目
(表面)※顔写真を入れたい。※協会サイトのQRコードを入れたい
名称:一般社団法人陽だまり暮らし支援会
役職&氏名:認定講師 ●●●●
住所:〒164-0012 東京都中野区本町4-8-3 (株)ヘルスアカデミア内
電話:03-5821-4476(平日9時~17時)
e-mail:info@kst-hrsa.example
URL:https://www.kst-hrsa.example/

(裏面)
協会の事業内容
平均寿命と健康寿命の乖離を少なくするための
・教育プログラムの提供
・フットケア施術者等の養成および派遣
・フットケア等の独立開業支援
・教材や物品等のの企画、開発、製造および販売
・協会会員の募集

※メモ欄を入れてください。
希望イメージ
シンプル 複雑
単色 カラフル
暗い 明るい
日常 高級
遊び心 厳粛
未来的 伝統的
女性的 男性的
希望する色
赤系、緑系
補足説明
ロゴを追加してください。
ふりがなをローマ字でいれてください。
①表面に下記の文言(協会の目指す内容)を入れてください。

平均寿命と健康寿命の乖離を少なくするために、、

②裏面の全内容を下記に変更願います。

<修了講座>
ソフトステップ®特別技術講座
・フットオイルマッサージ
・足底ケア
・爪ケア

<認定資格>
ソフトステップ®認定講師 フットオイルマッサージ
アクティブリズム® スペシャリスト

<お問い合わせ>
一般社団法人陽だまり暮らし支援協会事務局
e-mail:info@kst-hrsa.example

※メモ欄(MEMO)を設けてください。
■ 選んだ理由

見やすい。協会のイメージにあう。

■ 提案者全員のお礼・コメント

このたびはたくさんのご提案ありがとうございざいました。
良いご提案が多く、選考に時間を要してしまいました。
今後ともよろしくお願いいたします。

```html
<!DOCTYPE html>
<html lang="ja">
<head>
<meta charset="utf-8">
<title>陽だまり暮らし支援会 名刺</title>
<link rel="stylesheet" href="https://fonts.googleapis.com/css2?family=Noto+Sans+JP:wght@400;500;700&family=Noto+Serif+JP:wght@500&display=swap">
<style>
  :root{
    --green:#1e7a3c;
    --green-dark:#17662f;
    --yellow:#ece63f;
    --orange:#e8962a;
    --ink:#333;
    --paper:#ffffff;
    --canvas:#f4f4f2;
    --rule:#9ccaa8;
  }
  *{box-sizing:border-box;margin:0;padding:0}
  html,body{width:841px;height:1200px;overflow:hidden;background:var(--canvas);font-family:"Noto Sans JP",sans-serif;color:var(--ink)}
  .card{position:absolute;left:70px;width:700px;height:424px;background:var(--paper);overflow:hidden;box-shadow:0 4px 14px rgba(0,0,0,.18)}
  .card--front{top:90px}
  .card--back{top:680px}

  /* front */
  .front-shape{position:absolute;inset:0}
  .portrait{position:absolute;left:30px;top:28px;width:120px;height:120px;border-radius:50%;border:5px solid var(--paper);background:radial-gradient(circle at 50% 40%,#e9e3df,#b9b4b2)}
  .tagline{position:absolute;left:330px;top:24px;font-size:15px;color:var(--orange);letter-spacing:.04em}
  .role{position:absolute;left:30px;top:216px;font-size:15px;color:var(--paper);letter-spacing:.05em}
  .role span{margin-left:14px;letter-spacing:.1em;font-size:17px}
  .name{position:absolute;left:30px;top:244px;font-family:"Noto Serif JP",serif;font-size:42px;color:var(--yellow);letter-spacing:.18em;font-weight:500}
  .name-roman{position:absolute;left:30px;top:304px;font-size:20px;color:var(--paper);font-style:italic;letter-spacing:.04em}
  .org-mark{position:absolute;left:462px;top:92px;width:74px;height:74px;border-radius:50%;background:var(--green)}
  .org-name{position:absolute;left:380px;top:186px;font-size:19px;color:var(--ink);letter-spacing:.05em}
  .address{position:absolute;left:380px;top:220px;font-size:11px;line-height:1.45;color:var(--ink)}
  .contacts{position:absolute;left:380px;top:292px;list-style:none;font-size:13px}
  .contacts li{display:flex;align-items:center;height:24px}
  .contacts svg{width:18px;height:18px;margin-right:8px;flex:none}
  .front-band{position:absolute;left:0;right:0;bottom:0;height:26px;background:var(--green)}

  /* back */
  .back-shape{position:absolute;inset:0}
  .course-col{position:absolute;top:22px;color:var(--paper);font-size:15px;line-height:1.65}
  .course-col--left{left:40px}
  .course-col--right{left:370px}
  .course-col h2{color:var(--yellow);font-size:16px;font-weight:700;margin-bottom:2px}
  .memo-title{position:absolute;top:204px;left:0;right:0;text-align:center;color:#6fb43f;font-size:24px;letter-spacing:.08em}
  .memo-line{position:absolute;left:40px;right:40px;height:0;border-top:1px solid var(--rule)}
  .inquiry{position:absolute;left:40px;bottom:22px;color:var(--yellow);font-size:16px;font-weight:700}
  .inquiry-divider{position:absolute;left:288px;bottom:14px;width:1px;height:46px;background:var(--paper)}
  .inquiry-detail{position:absolute;left:310px;bottom:16px;color:var(--paper);font-size:14px;line-height:1.5}
</style>
</head>
<body>

<section class="card card--front">
  <svg class="front-shape" viewBox="0 0 700 424" width="700" height="424" aria-hidden="true">
    <path d="M0 0 H230 Q360 190 285 424 H0 Z" fill="var(--green)"/>
  </svg>
  <div class="portrait" role="img" aria-label="講師の顔写真"></div>
  <p class="tagline">平均寿命と健康寿命の乖離を少なくするために、、</p>
  <p class="role">認定講師<span>●●●●</span></p>
  <p class="name">森川 結衣</p>
  <p class="name-roman">Yui Morikawa</p>

  <div class="org-mark"></div>
  <p class="org-name">一般社団法人陽だまり暮らし支援会</p>
  <p class="address">〒164-0012 東京都中野区本町4-8-3<br>(株)ヘルスアカデミア内</p>
  <ul class="contacts">
    <li><svg viewBox="0 0 20 20"><circle cx="10" cy="10" r="10" fill="var(--green)"/><path d="M7 5.5l2 2-1 1.3c.6 1.4 1.7 2.5 3.2 3.2l1.3-1 2 2-1.2 1.5c-3.8-.4-7.3-3.9-7.6-7.7z" fill="#fff"/></svg>03-5821-4476（平日9時～17時）</li>
    <li><svg viewBox="0 0 20 20"><circle cx="10" cy="10" r="10" fill="var(--green)"/><rect x="5" y="6.5" width="10" height="7" fill="none" stroke="#fff" stroke-width="1.3"/><path d="M5 6.5l5 4 5-4" fill="none" stroke="#fff" stroke-width="1.3"/></svg>info@kst-hrsa.example</li>
    <li><svg viewBox="0 0 20 20"><circle cx="10" cy="10" r="10" fill="var(--green)"/><rect x="5" y="5.5" width="10" height="9" rx="1" fill="none" stroke="#fff" stroke-width="1.3"/><path d="M5 8.5h10" stroke="#fff" stroke-width="1.3"/></svg>https://www.kst-hrsa.example/</li>
  </ul>
  <div class="front-band"></div>
</section>

<section class="card card--back">
  <svg class="back-shape" viewBox="0 0 700 424" width="700" height="424" aria-hidden="true">
    <rect x="0" y="0" width="700" height="424" fill="var(--green)"/>
    <path d="M0 220 Q350 115 700 220 V350 H0 Z" fill="var(--paper)"/>
  </svg>
  <div class="course-col course-col--left">
    <h2>&lt;修了講座&gt;</h2>
    <p>ソフトステップ®特別技術講座</p>
    <p>・フットオイルマッサージ</p>
    <p>・足底ケア</p>
    <p>・爪ケア</p>
  </div>
  <div class="course-col course-col--right">
    <h2>&lt;認定資格&gt;</h2>
    <p>ソフトステップ®認定講師</p>
    <p>フットオイルマッサージ</p>
    <p>アクティブリズム® スペシャリスト</p>
  </div>
  <p class="memo-title">MEMO</p>
  <div class="memo-line" style="top:246px"></div>
  <div class="memo-line" style="top:280px"></div>
  <div class="memo-line" style="top:314px"></div>
  <p class="inquiry">&lt;お問い合わせ&gt;</p>
  <div class="inquiry-divider"></div>
  <p class="inquiry-detail">一般社団法人陽だまり暮らし支援協会事務局<br>e-mail : info@kst-hrsa.example</p>
</section>

</body>
</html>
```